Bright Harbor Coverage Partners
Auto-Home-Health-Business
Project: Bright Harbor Coverage Partners
Bright Harbor Coverage Partners - Consulting
Creative Brief
Professional
Dario F Menzel
Insurance Broker
4287 Willowgate Pkwy, suite D Rancho Cucamonga,CA,91458
mtorvel@bhcpins.com
0K52718
I need to more sets of business cards for my partners
I would like the logo

```html
<!DOCTYPE html>
<html lang="en">
<head>
<meta charset="utf-8">
<title>Bright Harbor Coverage Partners – Business Card</title>
<link href="https://fonts.googleapis.com/css2?family=Cinzel:wght@400;600&family=Open+Sans:wght@400;600&display=swap" rel="stylesheet">
<style>
  :root{
    --backdrop:#e9e6e1;
    --card-white:#ffffff;
    --navy:#1b2f6b;
    --blue-deep:#0b2a6e;
    --blue-mid:#1d4fa3;
    --blue-light:#3a6fc4;
    --ink:#2a2a2a;
    --logo-white:#ffffff;
  }
  *{margin:0;padding:0;box-sizing:border-box}
  html,body{width:1200px;height:442px;overflow:hidden;background:var(--backdrop)}
  .sheet{position:relative;width:1200px;height:442px}
  .card{
    position:absolute;top:71px;width:560px;height:300px;border-radius:18px;overflow:hidden;
    box-shadow:0 4px 14px rgba(0,0,0,.25);
  }
  .card--front{left:30px;background:var(--card-white)}
  .card--back{
    left:610px;
    background:linear-gradient(180deg,var(--blue-deep) 0%,var(--blue-mid) 50%,var(--blue-deep) 100%);
  }
  .card--back .band{
    position:absolute;left:0;right:0;top:92px;height:116px;
    background:linear-gradient(180deg,rgba(255,255,255,0) 0%,rgba(120,170,240,.25) 50%,rgba(255,255,255,0) 100%);
    border-top:1px solid rgba(255,255,255,.15);border-bottom:1px solid rgba(255,255,255,.15);
  }
  .holder{position:absolute;top:24px;left:0;right:0;text-align:center}
  .holder__name{font-family:"Cinzel",serif;font-weight:600;font-size:25px;color:var(--navy);letter-spacing:.5px}
  .holder__title{font-family:"Open Sans",sans-serif;font-size:12px;color:var(--ink);margin-top:2px}
  .card--front .band{
    position:absolute;left:0;right:0;top:98px;height:118px;
    background:linear-gradient(180deg,var(--blue-deep) 0%,var(--blue-light) 50%,var(--blue-deep) 100%);
  }
  .lockup{
    position:absolute;left:0;right:0;top:50%;transform:translateY(-50%);
    display:flex;align-items:center;justify-content:center;gap:14px;
  }
  .lockup__dot{width:46px;height:46px;border-radius:50%;border:2px solid var(--logo-white)}
  .lockup__name{font-family:"Cinzel",serif;font-weight:600;font-size:24px;line-height:1.05;color:var(--logo-white)}
  .contact{position:absolute;left:0;right:0;top:230px;text-align:center;font-family:"Open Sans",sans-serif;color:var(--ink)}
  .contact__line{font-size:11.5px;display:flex;justify-content:center;align-items:center;gap:8px}
  .contact__item{display:inline-flex;align-items:center;gap:3px}
  .contact__item svg{width:11px;height:11px;fill:var(--navy)}
  .contact__address{font-size:11.5px;margin-top:6px}
  .license{position:absolute;right:22px;bottom:10px;font-family:"Open Sans",sans-serif;font-size:7.5px;color:var(--ink)}
</style>
</head>
<body>
<div class="sheet">
  <section class="card card--front">
    <div class="holder">
      <div class="holder__name">DARIO F MENZEL</div>
      <div class="holder__title">Insurance Broker</div>
    </div>
    <div class="band">
      <div class="lockup">
        <span class="lockup__dot"></span>
        <span class="lockup__name">BRIGHT HARBOR<br>COVERAGE PARTNERS</span>
      </div>
    </div>
    <div class="contact">
      <div class="contact__line">
        <span class="contact__item"><svg viewBox="0 0 24 24"><path d="M6.6 10.8a15 15 0 0 0 6.6 6.6l2.2-2.2a1 1 0 0 1 1-.25 11.4 11.4 0 0 0 3.6.57 1 1 0 0 1 1 1V20a1 1 0 0 1-1 1A17 17 0 0 1 3 4a1 1 0 0 1 1-1h3.5a1 1 0 0 1 1 1c0 1.25.2 2.45.57 3.6a1 1 0 0 1-.25 1z"/></svg>(555)214-3086</span>
        <span class="contact__item"><svg viewBox="0 0 24 24"><rect x="7" y="2" width="10" height="20" rx="2"/></svg>(555)382-6041</span>
        <span class="contact__item"><svg viewBox="0 0 24 24"><rect x="3" y="9" width="18" height="9" rx="1"/><rect x="7" y="3" width="10" height="6"/></svg>(555)607-1925</span>
        <span class="contact__item"><svg viewBox="0 0 24 24"><path d="M2 5h20v14H2zM2 5l10 8 10-8" fill="none" stroke="#1b2f6b" stroke-width="2"/></svg>mtorvel@bhcpins.com</span>
      </div>
      <div class="contact__address">4287 Willowgate Pkwy, suite D Rancho Cucamonga,CA,91458</div>
    </div>
    <div class="license">License No.: 0K52718</div>
  </section>

  <section class="card card--back">
    <div class="band"></div>
    <div class="lockup">
      <span class="lockup__dot"></span>
      <span class="lockup__name">BRIGHT HARBOR<br>COVERAGE PARTNERS</span>
    </div>
  </section>
</div>
</body>
</html>
```